Trindle Salve by Petal Wrens: All Natural Lip Balm Co. Looking for New Label

Greetings, our company is called Petal Wrens and we are a start-up founded in early 2014. We make 100% All-Natural lip balm, called Trindle Salve, in a variety of flavors and we are looking for a new label that incorporates part of our logo and highlights our product name and our lip balms flavor (see attached files). Our website is: trindlesalve.example, and we are on Twitter: @PetalWrensSalves, and Facebook: /PetalWrensSalves. Our lip balms are made with beeswax, sweet almond oil, shea butter, coconut oil and other all natural oils and flavors.

The design should be clean, and communicate comfort, its "all-natural-ness", reliability, and fun. The colors we would like to have incorporated are burgundy, a deep, but not dark orange (see files, website, logo, graphics), some green and maybe gold/yellow. Given that the lip balm tubes are small (standard tubes), we would like to assure that the lip balm name, the flavor, and part of the logo- (perhaps the bee), are clearly visible and easily read. I am open to a variety of fonts, as long as they convey what I have stated above.

We want to use the label graphics and our logo for not only labeling our product, but also for use on our website, on banners, signs, retail boxes, letterhead, tee shirts, etc. If we like the design we are open to working with you again as our company is growing and we will be expanding our product line within the year to include hand and body balms, as well as other similar items and we will eventually have a few different product lines marketed at various age groups as well. Our lip balm is currently marketed to 14 to 40+ demographic, with the average age being roughly in the 15 to 24 range and our lip balm has been purchased by more women than men, though we market to both.

As far as software goes, I would like it to be in a format that is most popular- my old logo and graphics were made in Adobe Creative Suite 5.0, Adobe InDesign, and Adobe Illustrator, so the label should be made using this software (or a higher version). If I can have the label in a JPEG format also so I personally can add it to my website and social media that would be great.

I have a label redesign doc in an indd format but it was too large to upload. I believe this was the entire layout of our last label. If you need this, or anything else, please let me know as well as how I can send it to you.

We have applied to the popular TV show Otter Court and recently received a call back with interest from the producers; we are so excited and hope you are as well!

Thank you!
Gregor Tallowby
Owner
Petal Wrens Salves LLC
Gregor@PetalWrensSalves.example

The Label dimensions are: 2.25 inches wide ---> by 2 inches long. Currently, there is a .75 inch area that is part of the label and is perforated, used as a safety seal. I may be changing the labels to a slightly different kind but the dimensions will be the same. The tubes we use are standard lip balm tubes with a net weight of .15 ounces ( the total length of the tube from the bottom turning piece to the top of the cap is just over 2.5 inches (this is NOT how large the label must be).We are discontinuing the 1 Hive, 2 Hive concepts ( for different consistencies of the balm) so that part of the label does not need to be included.Feel free to enhance and/or modify the logo to fit the design of the label.Thank you! Added Thursday, February 12, 2015

Requirements
Must have
• Label Dimensions:
• Length: 2.125" Height: 2.125"
• Top Margin: 1.025" Bottom Margin: 1.025"
• Left Margin: 0.9125" Right Margin: 0.9125"
• Horizontal Spacing: 0.15" Vertical Spacing: 0.15"
• Horizontal Pitch: 2.275" Vertical Pitch: 2.275"

```html
<!DOCTYPE html>
<html lang="en">
<head>
<meta charset="utf-8">
<title>Trindlesalve Lip Balm Labels</title>
<link rel="stylesheet" href="https://fonts.googleapis.com/css2?family=Poiret+One&display=swap">
<style>
  :root {
    --page: #ffffff;
    --label-pink: #fce4dd;
    --comb-peach: #f9cfa3;
    --frame-grey: #a9a9a9;
    --perforation: #4a4a4a;
    --brand-green: #5ef21c;
    --flavor-orange: #f58a2a;
    --flavor-brown: #6e6560;
    --caption-grey: #6a6463;
    --side-burgundy: #a8262a;
    --bee-orange: #f39a2c;
    --bee-dark: #2b2118;
    --wing-green: #7fd36a;
  }
  * { margin: 0; padding: 0; box-sizing: border-box; }
  html, body {
    width: 1200px;
    height: 608px;
    overflow: hidden;
    background: var(--page);
  }
  .sheet {
    position: relative;
    width: 1200px;
    height: 608px;
  }
  .label {
    position: absolute;
    top: 75px;
    width: 465px;
    height: 414px;
    border: 2px solid var(--frame-grey);
    overflow: hidden;
    font-family: "Poiret One", sans-serif;
  }
  .label--orange { left: 22px; }
  .label--cookie { left: 704px; }

  .label__comb {
    position: absolute;
    inset: 0;
    background:
      radial-gradient(ellipse at 20% 15%, var(--comb-peach) 0%, transparent 55%),
      radial-gradient(ellipse at 55% 70%, var(--comb-peach) 0%, transparent 55%),
      radial-gradient(ellipse at 90% 30%, var(--comb-peach) 0%, transparent 50%),
      var(--label-pink);
  }

  .label__seal-line {
    position: absolute;
    left: 307px;
    top: 0;
    height: 100%;
    width: 3px;
  }

  .label__brand {
    position: absolute;
    left: 24px;
    top: 84px;
    font-size: 52px;
    font-weight: 400;
    line-height: 1;
    color: var(--brand-green);
    letter-spacing: 0.5px;
    white-space: nowrap;
  }
  .label__flavor {
    position: absolute;
    top: 144px;
    font-size: 26px;
    line-height: 1;
    white-space: nowrap;
  }
  .label--orange .label__flavor { left: 71px; color: var(--flavor-orange); }
  .label--cookie .label__flavor { left: 71px; color: var(--flavor-brown); }

  .label__caption {
    position: absolute;
    left: 167px;
    top: 193px;
    font-size: 17px;
    color: var(--caption-grey);
    white-space: nowrap;
  }

  .label__side-text {
    position: absolute;
    left: 389px;
    top: 12px;
    writing-mode: vertical-rl;
    font-size: 23px;
    line-height: 1;
    color: var(--side-burgundy);
    white-space: nowrap;
  }

  .label__bee {
    position: absolute;
    left: 20px;
    top: 232px;
    width: 170px;
    height: 165px;
    border-radius: 50%;
    background: radial-gradient(circle at 55% 55%, var(--bee-orange) 0%, var(--bee-orange) 35%, rgba(43,33,24,0.55) 55%, rgba(127,211,106,0.5) 70%, transparent 72%);
  }
  .label__mini-bee {
    position: absolute;
    left: 332px;
    top: 218px;
    width: 50px;
    height: 182px;
    background: linear-gradient(180deg, transparent 0%, rgba(43,33,24,0.12) 40%, rgba(243,154,44,0.75) 78%, rgba(127,211,106,0.6) 100%);
    border-radius: 25px;
  }
</style>
</head>
<body>
<main class="sheet">

  <section class="label label--orange">
    <div class="label__comb" role="img" aria-label="Honeycomb pattern of peach hexagons on pale pink"></div>
    <svg class="label__seal-line" viewBox="0 0 3 414" aria-hidden="true">
      <line x1="1.5" y1="0" x2="1.5" y2="414" stroke="var(--perforation)" stroke-width="2" stroke-dasharray="14 8"/>
    </svg>
    <h1 class="label__brand">Trindlesalve</h1>
    <p class="label__flavor">Orange Creampop</p>
    <p class="label__caption">beewax lip balm</p>
    <div class="label__bee" role="img" aria-label="Illustration of a cheerful orange and black striped bee with green wings"></div>
    <div class="label__mini-bee" role="img" aria-label="Small bee illustration trailing a dashed looping flight path"></div>
    <p class="label__side-text">Petal Wrens All Natural Lip Balm</p>
  </section>

  <section class="label label--cookie">
    <div class="label__comb" role="img" aria-label="Honeycomb pattern of peach hexagons on pale pink"></div>
    <svg class="label__seal-line" viewBox="0 0 3 414" aria-hidden="true">
      <line x1="1.5" y1="0" x2="1.5" y2="414" stroke="var(--perforation)" stroke-width="2" stroke-dasharray="14 8"/>
    </svg>
    <h1 class="label__brand">Trindlesalve</h1>
    <p class="label__flavor">Brown Sugar cookie</p>
    <p class="label__caption">beewax lip balm</p>
    <div class="label__bee" role="img" aria-label="Illustration of a cheerful orange and black striped bee with green wings"></div>
    <div class="label__mini-bee" role="img" aria-label="Small bee illustration trailing a dashed looping flight path"></div>
    <p class="label__side-text">Petal Wrens All Natural Lip Balm</p>
  </section>

</main>
</body>
</html>
```